Create a 3-4 page concept for an electrical contracting company

We are a company that requires a new look for our website. We are familiar with Sitecraft to be able to update using any theme or builder supplied.

While typical ideas of construction may get the yellow and blue colour pallette, hard hats, hammers, or lightning bolts entering the arena, we are completely against this image.

We intend for the website to have instant appeal and intuitive navigation. The home page should have a creative use of angles or brand identification with the banner or menubar if needed.

After combing hundreds of sitecraft templates, the most attractive seem to be aimed at beauty services. Unfortunately we do not have a lot of picture perfect material to showcase, but it can be blended in other ways. - the brand should be recognizable and captivating.

Target Market(s)

High-end contracting firms focused on quality and service for long term projects (Custom Homes)

Industry/Entity Type

Contracting

Font styles to use
Sans Serif
Other font styles liked:
• Gotham usually. Adjusted kerning and rounded edges seem to be more friendly

Requirements
Must have
• Creative use of the logo shape and colour scheme, especially at the home.

Use of a CMS to be modifiable from a browser (Sitecraft,etc) - A builder such as tandem, kora, or framewell accepted!

Elements or sections that could be adaptable for use. About us, members, contact, services... etc. Content would be written after
Nice to have
• Some clean inspiration that we appreciate:

www.harbelmedia.ca
www.pinwoodbuildworks.com
Should not have
• Generic welcome banner...

```html
<!DOCTYPE html>
<html lang="en">
<head>
<meta charset="utf-8">
<title>Larchmont Electric — Home</title>
<link rel="stylesheet" href="https://fonts.googleapis.com/css2?family=Anton&family=Montserrat:wght@600;700&family=Poppins:wght@400;500;600&display=swap">
<style>
:root{
  --blue:#1c84c0;
  --navy:#35566f;
  --ink:#1d2329;
  --text:#333a40;
  --muted:#5d656c;
  --band-a:#18242f;
  --band-b:#2e4a61;
  --white:#ffffff;
}
*{margin:0;padding:0;box-sizing:border-box}
html,body{width:1200px;height:2655px;overflow:hidden;background:var(--white)}
body{position:relative;font-family:"Poppins",sans-serif;color:var(--text)}
.abs{position:absolute}
a{color:inherit;text-decoration:none}

/* header */
.brand{display:flex;align-items:center;gap:10px;white-space:nowrap}
.brand-dot{width:14px;height:14px;border-radius:50%;background:var(--blue)}
.brand-name{font-family:"Poppins",sans-serif;font-weight:500;color:var(--ink);letter-spacing:.3px}
.site-brand{left:165px;top:33px}
.site-brand .brand-name{font-size:18px}
.main-nav{top:39px;left:508px;display:flex;gap:22px;font-size:11.5px;text-transform:uppercase;color:var(--ink)}
.main-nav .active{color:var(--blue);position:relative}
.main-nav .active::before{content:"";position:absolute;left:50%;top:-40px;width:1px;height:28px;background:var(--blue)}
.main-nav .active::after{content:"";position:absolute;left:calc(50% - 4px);top:-13px;width:6px;height:6px;border:1px solid var(--blue);border-radius:50%}
.nav-divider{left:886px;top:34px;width:1px;height:26px;background:#d6dbe0}
.nav-phone{left:897px;top:29px;display:flex;align-items:center;gap:6px;font-family:"Montserrat",sans-serif;font-weight:600;font-size:15.5px;color:var(--ink)}
.nav-phone .ring{width:34px;height:34px;border-radius:50%;background:var(--blue);display:flex;align-items:center;justify-content:center}

/* hero */
.hero-title{left:217px;top:128px;font-family:"Anton",sans-serif;font-size:50px;line-height:54px;color:var(--ink);letter-spacing:.5px}
.hero-title em{font-style:normal;color:var(--blue)}
.hero-sub{left:222px;top:240px;font-size:14px;color:var(--ink)}
.btn{display:flex;align-items:center;justify-content:center;background:var(--blue);color:var(--white);font-family:"Montserrat",sans-serif;font-weight:600;font-size:15px}
.hero-btn{left:222px;top:275px;width:142px;height:41px;z-index:2}
.hero-photo{left:57px;top:293px;width:1086px;height:457px;background:linear-gradient(100deg,#cfd2d1 0%,#a6a39d 35%,#e4e0d9 55%,#8d8d8a 80%,#4a2f24 100%)}
.slider-dashes{left:88px;top:725px;display:flex;gap:6px}
.slider-dashes span{width:24px;height:3px;background:var(--white)}
.slider-dashes span.on{background:var(--blue)}
.quote-card{left:626px;top:668px;width:412px;height:262px;background:var(--blue);color:var(--white);padding:42px 55px}
.quote-mark{font-family:"Poppins",sans-serif;font-size:72px;line-height:56px;height:40px;font-weight:400}
.quote-text{margin-top:14px;font-size:12.5px;line-height:22.5px}
.quote-name{margin-top:14px;font-size:13.5px;font-weight:500;display:flex;align-items:center;gap:10px}
.quote-name::before{content:"";width:11px;height:2px;background:var(--white)}
.quote-site{margin-left:21px;font-size:11px}

/* about */
.about-photo{left:212px;top:930px;width:413px;height:398px;background:linear-gradient(160deg,#e9e6e1 0%,#c9c2b8 50%,#6d5848 80%,#bfb7ad 100%)}
.about-title{left:698px;top:996px;font-family:"Montserrat",sans-serif;font-weight:700;font-size:33px;line-height:38px;color:var(--navy)}
.about-title span{color:var(--blue)}
.about-lead{left:698px;top:1085px;width:300px;font-size:14px;line-height:23px;color:var(--ink)}
.about-copy{left:701px;top:1141px;width:290px;font-size:12px;line-height:21px;color:var(--muted)}
.about-btn{left:702px;top:1241px;width:142px;height:41px}

/* services */
.services-title{left:0;top:1425px;width:1200px;text-align:center;font-family:"Montserrat",sans-serif;font-weight:700;font-size:31px;color:var(--navy)}
.services-title span{color:var(--blue)}
.services-copy{left:0;top:1475px;width:1200px;text-align:center;font-size:12.5px;line-height:23px;color:var(--muted)}
.service{top:1572px;width:160px;text-align:center;font-family:"Montserrat",sans-serif;font-weight:600;font-size:14.5px;line-height:21px;color:var(--navy)}
.service svg{display:block;margin:0 auto 32px}
.service.current{color:var(--blue)}

/* portfolio */
.portfolio-band{left:57px;top:1778px;width:1086px;height:629px;background:linear-gradient(90deg,var(--band-a) 0%,var(--band-b) 100%)}
.portfolio-photo{left:161px;top:1856px;width:668px;height:449px;background:linear-gradient(135deg,#dcdcd8 0%,#f1f0ec 45%,#a9a59f 75%,#5b3e2e 100%)}
.portfolio-card{left:703px;top:1956px;width:299px;height:300px;background:var(--blue);color:var(--white);padding:50px 38px}
.portfolio-card h2{font-family:"Montserrat",sans-serif;font-weight:700;font-size:32px;line-height:37px}
.portfolio-card p{margin-top:20px;font-size:12.5px;line-height:22.5px}
.slider-dots{left:565px;top:2326px;display:flex;gap:7px}
.slider-dots span{width:9px;height:9px;border-radius:50%;border:1px solid var(--white)}
.slider-dots span.on{background:var(--blue);border-color:var(--blue)}

/* footer */
.footer-brand{left:172px;top:2487px}
.footer-brand .brand-dot{width:20px;height:20px}
.footer-brand .brand-name{font-size:24px}
.socials{left:252px;top:2543px;display:flex;gap:6px}
.socials span{width:32px;height:32px;border-radius:50%;background:var(--navy)}
.socials span + span{background:var(--blue)}
.copyright{left:168px;top:2587px;font-size:10.5px;color:var(--text)}
.footer-head{font-family:"Montserrat",sans-serif;font-weight:600;font-size:14.5px;color:var(--navy)}
.sitemap{left:555px;top:2452px}
.sitemap ul{list-style:none;margin-top:20px}
.sitemap li{font-size:11.5px;line-height:24px;color:var(--text);padding-left:20px;position:relative}
.sitemap li::before{content:"";position:absolute;left:3px;top:10px;width:4px;height:4px;border-radius:50%;background:var(--blue)}
.contact{left:821px;top:2452px}
.contact-item{display:flex;gap:14px;margin-top:20px;font-size:11.5px;line-height:19px;color:var(--text)}
.contact-item + .contact-item{margin-top:12px}
.contact-item svg{flex:none;margin-top:3px}
</style>
</head>
<body>

<header>
  <div class="abs brand site-brand"><span class="brand-dot"></span><span class="brand-name">Larchmont Electric</span></div>
  <nav class="abs main-nav">
    <a class="active" href="#">Home</a><a href="#">Services</a><a href="#">Testimonials</a><a href="#">Portfolio</a><a href="#">Contact</a>
  </nav>
  <span class="abs nav-divider"></span>
  <div class="abs nav-phone">
    <span class="ring"><svg width="16" height="16" viewBox="0 0 24 24" fill="none" stroke="#fff" stroke-width="1.8"><path d="M5 3h4l2 5-2.5 1.5a11 11 0 0 0 6 6L16 13l5 2v4a2 2 0 0 1-2 2A17 17 0 0 1 3 5a2 2 0 0 1 2-2z"/></svg></span>
    123 456 7890
  </div>
</header>

<section class="hero">
  <h1 class="abs hero-title">We Aren’t <em>Satisfied</em><br>Until You Are.</h1>
  <p class="abs hero-sub">We Work With Innovation, &amp; Growing with Advancements Technology</p>
  <a class="abs btn hero-btn" href="#">CONTACT US</a>
  <div class="abs hero-photo" role="img" aria-label="Modern open-plan living room with a white sectional sofa, large windows and a pendant lamp over the kitchen"></div>
  <div class="abs slider-dashes"><span class="on"></span><span></span><span></span><span></span></div>
  <blockquote class="abs quote-card">
    <div class="quote-mark">“</div>
    <p class="quote-text">" Lorem Ipsum is simply dummy text of the printing and typesetting industry. Lorem Ipsum has been the industry's standard ".</p>
    <p class="quote-name">Client Name</p>
    <p class="quote-site">something.com</p>
  </blockquote>
</section>

<section class="about">
  <div class="abs about-photo" role="img" aria-label="Bright dining room with a glass table, white chairs and recessed ceiling lights"></div>
  <h2 class="abs about-title">LARCHMONT<br><span>ELECTRIC</span></h2>
  <p class="abs about-lead">Our Dedications are in the Needs of the Clients, and our aim is to Surpass them.</p>
  <p class="abs about-copy">We are a North Shore electrical contracting company. We are a fresh look on the industry; marrying tradition with innovation, and growing with advancements of our field's technology .</p>
  <a class="abs btn about-btn" href="#">KNOW MORE</a>
</section>

<section class="services">
  <h2 class="abs services-title">WHAT CAN WE <span>DO FOR YOU?</span></h2>
  <p class="abs services-copy">Our vision is to continue tradition of outstanding workmanship with<br>uncompromising quality and personalized approach.</p>

  <div class="abs service current" style="left:164px">
    <svg width="66" height="62" viewBox="0 0 66 62" fill="none" stroke="#1d2329" stroke-width="2"><path d="M12 28 33 8l21 20M17 24v22h32V24"/><rect x="27" y="30" width="12" height="16" fill="#1c84c0" stroke="#1d2329"/><circle cx="33" cy="20" r="3"/><path d="M2 56h62M33 46v10"/></svg>
    Whole Home<br>Electrical
  </div>
  <div class="abs service" style="left:343px">
    <svg width="66" height="62" viewBox="0 0 66 62" fill="none" stroke="#1d2329" stroke-width="2"><path d="M14 34 33 18l19 16v24H14z"/><path d="M26 58V44h14v14"/><path d="M27 30h12l-6-8z" fill="#1c84c0"/><path d="M24 12a12 12 0 0 1 18 0M20 7a18 18 0 0 1 26 0"/></svg>
    Home<br>Automation
  </div>
  <div class="abs service" style="left:521px">
    <svg width="66" height="62" viewBox="0 0 66 62" fill="none" stroke="#1d2329" stroke-width="2"><circle cx="33" cy="22" r="18"/><path d="M19 34a18 18 0 0 0 28 0" stroke="#1c84c0" stroke-width="5"/><path d="M25 40v8h16v-8M18 48h30v10H18z"/><circle cx="27" cy="18" r="1.5" fill="#1d2329"/><circle cx="33" cy="14" r="1.5" fill="#1d2329"/><circle cx="39" cy="18" r="1.5" fill="#1d2329"/><circle cx="33" cy="22" r="1.5" fill="#1d2329"/><circle cx="27" cy="26" r="1.5" fill="#1d2329"/><circle cx="39" cy="26" r="1.5" fill="#1d2329"/></svg>
    Landscape<br>Lighting
  </div>
  <div class="abs service" style="left:697px">
    <svg width="66" height="62" viewBox="0 0 66 62" fill="none" stroke="#1d2329" stroke-width="2"><rect x="12" y="2" width="42" height="58"/><rect x="26" y="18" width="14" height="26"/><rect x="33" y="24" width="7" height="20" fill="#1c84c0"/><circle cx="18" cy="8" r="2"/><circle cx="48" cy="8" r="2"/><circle cx="18" cy="54" r="2"/><circle cx="48" cy="54" r="2"/></svg>
    Backup<br>Power
  </div>
  <div class="abs service" style="left:877px">
    <svg width="66" height="62" viewBox="0 0 66 62" fill="none" stroke="#1d2329" stroke-width="2"><rect x="6" y="4" width="54" height="30"/><path d="M6 12h54" stroke="#1c84c0" stroke-width="6"/><circle cx="40" cy="19" r="7"/><path d="M38 16v6l5-3z" fill="#1d2329"/><path d="M4 40h58v8H4zM4 52h58v8H4z"/></svg>
    Media &amp;<br>Entertainment
  </div>
</section>

<section class="portfolio">
  <div class="abs portfolio-band"></div>
  <div class="abs portfolio-photo" role="img" aria-label="Kitchen with a marble island, pendant globe lights and a dining area by the windows"></div>
  <div class="abs portfolio-card">
    <h2>OUR<br>PORTFOLIO</h2>
    <p>Established in North Vancouver, Larchmont Electric has a history of work in the finest custom projects, to the complexities of any scale of renovation</p>
  </div>
  <div class="abs slider-dots"><span></span><span class="on"></span><span></span><span></span><span></span></div>
</section>

<footer>
  <div class="abs brand footer-brand"><span class="brand-dot"></span><span class="brand-name">Larchmont Electric</span></div>
  <div class="abs socials"><span></span><span></span></div>
  <p class="abs copyright">©LARCHMONT ELECTRIC- 2020 All rights reserved.</p>

  <div class="abs sitemap">
    <h3 class="footer-head">SITEMAP</h3>
    <ul><li>Home</li><li>Services</li><li>Testimonials</li><li>Portfolio</li><li>Contact</li></ul>
  </div>

  <div class="abs contact">
    <h3 class="footer-head">CONTACT US</h3>
    <div class="contact-item">
      <svg width="14" height="14" viewBox="0 0 24 24" fill="#1c84c0"><path d="M5 2h4l2 6-3 2a12 12 0 0 0 6 6l2-3 6 2v4a3 3 0 0 1-3 3A18 18 0 0 1 2 5a3 3 0 0 1 3-3z"/></svg>
      <div>Owen Pratt<br>(604) 555-0148</div>
    </div>
    <div class="contact-item">
      <svg width="14" height="14" viewBox="0 0 24 24" fill="#1c84c0"><path d="M5 2h4l2 6-3 2a12 12 0 0 0 6 6l2-3 6 2v4a3 3 0 0 1-3 3A18 18 0 0 1 2 5a3 3 0 0 1 3-3z"/></svg>
      <div>Daniel Reyes<br>(604) 555-0172</div>
    </div>
    <div class="contact-item">
      <svg width="15" height="12" viewBox="0 0 24 18" fill="#1c84c0"><path d="M0 0h24v18H0z"/><path d="M1 1l11 9 11-9" stroke="#fff" stroke-width="2" fill="none"/></svg>
      <div>office@larchmontelectric.ca</div>
    </div>
  </div>
</footer>

</body>
</html>
```